Business Card for a recruitment agency specializing in engineers and geeks.

I am looking to create Business Card Design for my company.
That
## Company name:
Quorvant Inc.
Quorvant is a term coined from the following concepts.
1. geek + engineer
2. geek utopia
## Company Description:
The concept of the company is to be a recruitment agency that creates a paradise for geeky engineers. We want to be a place where engineers can have more freedom and ideal career support.
# Target.
The noun itself is often given to companies that want to hire engineers, geeks, and IT-related personnel, so it would be nice to get the impression that this company seems to have good engineers and IT personnel. There are many occasions where I meet with the human resources department, president, or senior management and give it to them.
# Atmosphere
We are happy with simplicity, but with an impact that will help people remember the company. The logo is based on a dinosaur that does programming, so it should be somewhat playful, but since it will basically be used in a business setting, please don't make it too silly.
# About the logo
See the attached files. The company logo represents our engineers smiling upward because of our work, with the motif of a dinosaur doing programming.
## Color
We will leave the color scheme to you, but since the logo is in black and white, colors with such a taste would fit well.
## file format
ai, psd, png, svg
Industry/Entity Type
human resource and employment agency
Contact Information for Business Card
Company name, address, email, tel, URL,logo
Colors
Designer to choose colors to be used in the design.

```html
<!DOCTYPE html>
<html lang="en">
<head>
<meta charset="UTF-8">
<title>Quorvant Inc. — Business Card</title>
<link href="https://fonts.googleapis.com/css2?family=Montserrat:wght@400;500;600;700&family=Open+Sans+Condensed:wght@700&display=swap" rel="stylesheet">
<style>
  :root {
    --backdrop: #2c2c2e;
    --ink: #0d0d0d;
    --card-dark: #101010;
    --paper: #ffffff;
    --rule: #1a1a1a;
    --muted: #3a3a3a;
  }
  * { box-sizing: border-box; margin: 0; padding: 0; }
  html, body { width: 1200px; height: 1095px; overflow: hidden; }
  body {
    background: var(--backdrop);
    font-family: "Montserrat", sans-serif;
    position: relative;
  }
  .card {
    position: absolute;
    width: 700px;
    height: 400px;
    border-radius: 22px;
    overflow: hidden;
  }

  /* Front */
  .card-front { left: 110px; top: 90px; background: var(--card-dark); }
  .front-pattern {
    position: absolute; inset: 0;
    background: radial-gradient(ellipse at 75% 20%, #3a3a3a 0%, #1a1a1a 45%, #0c0c0c 100%);
  }
  .front-wordmark {
    position: absolute; left: 0; right: 0; top: 150px;
    display: flex; align-items: center; justify-content: center; gap: 18px;
    color: var(--paper);
  }
  .wordmark-square { width: 38px; height: 38px; background: var(--paper); }
  .front-wordmark .name { font-weight: 600; font-size: 62px; letter-spacing: 1px; line-height: 1; }
  .tagline-band {
    position: absolute; left: 0; right: 0; top: 298px; height: 36px;
    background: var(--paper);
    display: flex; align-items: center; justify-content: center;
    padding: 0 20px;
  }
  .tagline {
    font-family: "Open Sans Condensed", sans-serif;
    font-weight: 700; font-size: 18px; line-height: 1; color: var(--ink);
    white-space: nowrap;
  }

  /* Back */
  .card-back { left: 390px; top: 565px; background: var(--paper); }
  .back-wordmark {
    position: absolute; left: 40px; top: 0; bottom: 0; width: 310px;
    display: flex; flex-direction: column; align-items: center; justify-content: center; gap: 28px;
    color: var(--ink);
  }
  .back-wordmark .wordmark-square { width: 96px; height: 96px; background: var(--ink); }
  .back-wordmark .name { font-weight: 600; font-size: 56px; letter-spacing: 1px; line-height: 1; }
  .divider {
    position: absolute; left: 372px; top: 70px; width: 2px; height: 260px; background: var(--rule);
  }
  .divider::after {
    content: ""; position: absolute; left: -1px; top: 60px; width: 4px; height: 90px; background: var(--ink);
  }
  .contact { position: absolute; left: 402px; top: 62px; width: 280px; color: var(--ink); }
  .person-name { font-weight: 700; font-size: 26px; letter-spacing: 1.5px; }
  .person-role { font-size: 15px; color: var(--muted); margin-top: 2px; letter-spacing: .5px; }
  .contact hr { border: 0; border-top: 1.5px solid var(--rule); margin: 12px 0; width: 220px; }
  .address { font-size: 16px; line-height: 1.55; letter-spacing: .8px; padding-left: 10px; }
  .lines { list-style: none; font-size: 15.5px; letter-spacing: 1.4px; line-height: 1.8; }
  .lines li { display: flex; align-items: center; gap: 10px; white-space: nowrap; }
  .lines svg { width: 13px; height: 13px; fill: var(--ink); flex: none; }
</style>
</head>
<body>
  <section class="card card-front">
    <div class="front-pattern" role="img" aria-label="Repeating glossy pattern of the brand symbol on black"></div>
    <div class="front-wordmark">
      <span class="wordmark-square"></span>
      <span class="name">Quorvant</span>
    </div>
    <div class="tagline-band">
      <p class="tagline">Full-time, freelance, and side-employment agents for IT and web professionals</p>
    </div>
  </section>

  <section class="card card-back">
    <div class="back-wordmark">
      <span class="wordmark-square"></span>
      <span class="name">Quorvant</span>
    </div>
    <div class="divider"></div>
    <div class="contact">
      <h1 class="person-name">MARC LEFEBRE</h1>
      <p class="person-role">Director</p>
      <hr>
      <p class="address">1187 Rue Pelletier Montréal,<br>QC H3K 1N4</p>
      <hr>
      <ul class="lines">
        <li><svg viewBox="0 0 24 24"><path d="M6.6 10.8a15 15 0 0 0 6.6 6.6l2.2-2.2c.3-.3.7-.4 1-.2 1.1.4 2.3.6 3.6.6.6 0 1 .4 1 1V20c0 .6-.4 1-1 1A17 17 0 0 1 3 4c0-.6.4-1 1-1h3.5c.6 0 1 .4 1 1 0 1.3.2 2.5.6 3.6.1.3 0 .7-.2 1z"/></svg>800-555-0147</li>
        <li><svg viewBox="0 0 24 24"><path d="M2 5h20v14H2z M2 5l10 8 10-8" fill="none" stroke="#0d0d0d" stroke-width="2"/><path d="M2 5h20l-10 8z"/></svg>firstname@quorvant.com</li>
        <li><svg viewBox="0 0 24 24"><circle cx="12" cy="12" r="10" fill="none" stroke="#0d0d0d" stroke-width="2"/><path d="M2 12h20M12 2c3 3 3 17 0 20M12 2c-3 3-3 17 0 20" fill="none" stroke="#0d0d0d" stroke-width="1.6"/></svg>www.quorvant.com</li>
      </ul>
    </div>
  </section>
</body>
</html>
```